Flyer for Mountain Bike Skills Event

Create an 11x17 posts for an upcoming Mountain Bike Skills event.

Falcon Trail Riding Academy Logo
--
Are you ready to ride your mountain bike faster and with more confidence? Join us to learn how to take your riding to the next level!
--
EVENT INFORMATION:

Saturday April 23
>> Fundamental Skills Clinic
>> Jumping Mini Clinic

Sunday April 24
>> Intermediate / Advanced Skills Clinic

Saturday - Sunday April 23/24
>> 2 Day Skills Camp

--
San Diego, California
--
Following your clinic, you will see an immediate improvement in your riding and a boost in confidence.

Skills taught and practiced in courses include:

Mind skills
Mastering manual front-wheel lifts
Manual dropping roots & steps
Cornering with speed & confidence
Reading & breaking down the trail
Introduction to energy management & flow
Linking trail sections for flow
Attacking flat corners
Flat and cambered corners
Bermed corners; lines and pumping
Switchbacks
Maximizing grip and traction with pumping
Learning to pump for speed & air

Event hosted by: HARLOWE CYCLE DEPOT (*use logo)

Sign up today!
--
More informaiton on our website:
WWW.PEDALWITHPOISE.COM

Target Market(s)

Mountain bikers age 35-60

Industry/Entity Type

Fitness

Requirements
Must have
• Falcon Logo
• Should be consistent with the Falcon brand, see website for examples: https://coastaltrailcraftlessons.com/ and our truck wrap design file.
• Flyer needs to be easy to read and include all the content in the project description.
Nice to have
• Include our tag line: SOAR LIKE A FALCON

```html
<!DOCTYPE html>
<html lang="en">
<head>
<meta charset="utf-8">
<title>Soar Like a Falcon – Mountain Bike Skills Event</title>
<link href="https://fonts.googleapis.com/css2?family=Anton&family=Bebas+Neue&family=Archivo+Black&family=Questrial&display=swap" rel="stylesheet">
<style>
  :root{
    --red:#e8141b;
    --ink:#1a1616;
    --paper:#e9e9e9;
    --paper-dark:#d4d4d4;
    --white:#ffffff;
    --sky-top:#3f6fae;
    --sky-mid:#8fb0d6;
    --earth:#7a6a55;
  }
  *{margin:0;padding:0;box-sizing:border-box}
  html,body{width:869px;height:1200px;overflow:hidden;background:#cfcfcf}
  .poster{
    position:relative;width:869px;height:1200px;overflow:hidden;
    background:radial-gradient(ellipse at 50% 60%, #f1f1f1 0%, var(--paper) 55%, var(--paper-dark) 100%);
    font-family:"Questrial",sans-serif;color:var(--ink);
  }
  .hero-photo{
    position:absolute;left:0;top:0;width:869px;height:520px;
    background:
      linear-gradient(180deg, rgba(233,233,233,0) 55%, var(--paper) 100%),
      linear-gradient(200deg, var(--sky-top) 0%, var(--sky-mid) 45%, var(--earth) 85%);
  }
  .brand-logo{
    position:absolute;left:69px;top:96px;width:330px;
    font-family:"Archivo Black",sans-serif;color:var(--ink);
    font-size:30px;line-height:1.05;text-transform:uppercase;
  }
  .headline{position:absolute;left:0;top:0;width:869px;height:640px}
  .headline text{font-family:"Anton",sans-serif}
  .slashes{position:absolute;left:700px;top:580px}
  .intro{
    position:absolute;left:56px;top:642px;font-size:26px;color:#2a2a2a;
  }
  .schedule{position:absolute;left:0;top:0}
  .event-row{position:absolute;display:flex;height:45px}
  .event-day{
    background:var(--red);color:var(--white);
    font-family:"Bebas Neue",sans-serif;font-size:25px;
    display:flex;align-items:center;padding-left:16px;
  }
  .event-arrow{width:22px;height:45px}
  .event-name{
    background:var(--ink);color:var(--white);
    font-family:"Archivo Black",sans-serif;font-size:17px;letter-spacing:.5px;
    display:flex;align-items:center;padding-left:20px;margin-left:-1px;
  }
  .skills-title{
    position:absolute;left:47px;top:874px;
    font-family:"Bebas Neue",sans-serif;font-size:27px;color:var(--red);
  }
  .skills-list{position:absolute;list-style:none;font-size:17.5px;line-height:21.3px;color:#262626}
  .skills-list li{display:flex;align-items:center;gap:6px}
  .skills-list svg{flex:none}
  .skills-left{left:47px;top:911px}
  .skills-right{left:451px;top:911px}
  .host{
    position:absolute;left:600px;top:1068px;display:flex;align-items:center;gap:10px;
  }
  .host-label{font-family:"Bebas Neue",sans-serif;font-size:23px}
  .host-logo{display:flex;align-items:center;gap:6px;font-family:"Questrial",sans-serif;font-size:11px;line-height:1.15;width:150px}
  .host-logo .dot{width:38px;height:38px;border-radius:50%;border:3px solid var(--ink);flex:none}
  .footer-rule{position:absolute;left:0;top:1128px;width:869px;height:5px;background:var(--ink)}
  .footer{
    position:absolute;left:0;top:1133px;width:869px;height:67px;background:var(--red);
    color:var(--white);display:flex;align-items:center;justify-content:center;font-size:22px;
  }
  .footer strong{font-family:"Archivo Black",sans-serif;font-weight:400;margin-left:6px}
</style>
</head>
<body>
<main class="poster">
  <div class="hero-photo" role="img" aria-label="Photo of a mountain biker in helmet and pads jumping a rocky desert trail against a blue sky"></div>

  <div class="brand-logo">Falcon Trail<br>Riding Academy</div>

  <svg class="headline" viewBox="0 0 869 640" aria-label="Soar like a Falcon. Are you ready to ride your mountain bike faster and with more confidence?">
    <text x="61" y="336" font-size="150" fill="var(--red)" textLength="370" lengthAdjust="spacingAndGlyphs">SOAR</text>
    <text x="444" y="338" font-size="78" fill="var(--white)" textLength="360" lengthAdjust="spacingAndGlyphs">LIKE A</text>
    <text x="61" y="492" font-size="180" fill="var(--red)" textLength="770" lengthAdjust="spacingAndGlyphs">FALCON</text>
    <text x="56" y="560" font-size="62" fill="var(--ink)" style="font-family:'Bebas Neue',sans-serif" textLength="772" lengthAdjust="spacingAndGlyphs">ARE YOU READY TO RIDE YOUR MOUNTAIN BIKE</text>
    <text x="56" y="622" font-size="62" fill="var(--ink)" style="font-family:'Bebas Neue',sans-serif" textLength="632" lengthAdjust="spacingAndGlyphs">FASTER AND WITH MORE CONFIDENCE?</text>
  </svg>

  <svg class="slashes" width="128" height="44" viewBox="0 0 128 44" aria-hidden="true">
    <polygon points="14,0 44,0 30,44 0,44" fill="var(--ink)"/>
    <polygon points="56,0 86,0 72,44 42,44" fill="var(--red)"/>
    <polygon points="98,0 128,0 114,44 84,44" fill="var(--ink)"/>
  </svg>

  <p class="intro">Join us to learn how to take your riding to the next level!</p>

  <div class="event-row" style="left:84px;top:698px">
    <div class="event-day" style="width:183px">SATURDAY APRIL 23</div>
    <svg class="event-arrow" viewBox="0 0 22 45" aria-hidden="true"><polygon points="0,0 22,22.5 0,45" fill="var(--red)"/></svg>
    <div class="event-name" style="width:516px;margin-left:-22px;padding-left:42px;word-spacing:2px">Fundamental Skills Clinic&nbsp;&nbsp;Jumping Mini Clinic</div>
  </div>
  <div class="event-row" style="left:124px;top:754px">
    <div class="event-day" style="width:172px">SUNDAY APRIL 24</div>
    <svg class="event-arrow" viewBox="0 0 22 45" aria-hidden="true"><polygon points="0,0 22,22.5 0,45" fill="var(--red)"/></svg>
    <div class="event-name" style="width:470px;margin-left:-22px;padding-left:52px">Intermediate / Advanced Skills Clinic</div>
  </div>
  <div class="event-row" style="left:188px;top:807px">
    <div class="event-day" style="width:282px">SATURDAY - SUNDAY APRIL 23/24</div>
    <svg class="event-arrow" viewBox="0 0 22 45" aria-hidden="true"><polygon points="0,0 22,22.5 0,45" fill="var(--red)"/></svg>
    <div class="event-name" style="width:262px;margin-left:-22px;padding-left:42px">2 Day Skills Camp</div>
  </div>

  <h2 class="skills-title">SKILLS TAUGHT AND PRACTICED IN COURSES INCLUDE:</h2>

  <ul class="skills-list skills-left">
    <li><svg width="14" height="12" viewBox="0 0 14 12"><polygon points="0,0 14,6 0,12 4,6" fill="#e8141b"/></svg>Mind skills</li>
    <li><svg width="14" height="12" viewBox="0 0 14 12"><polygon points="0,0 14,6 0,12 4,6" fill="#e8141b"/></svg>Mastering manual front-wheel lifts</li>
    <li><svg width="14" height="12" viewBox="0 0 14 12"><polygon points="0,0 14,6 0,12 4,6" fill="#e8141b"/></svg>Manual dropping roots &amp; steps</li>
    <li><svg width="14" height="12" viewBox="0 0 14 12"><polygon points="0,0 14,6 0,12 4,6" fill="#e8141b"/></svg>Cornering with speed &amp; confidence</li>
    <li><svg width="14" height="12" viewBox="0 0 14 12"><polygon points="0,0 14,6 0,12 4,6" fill="#e8141b"/></svg>Reading &amp; breaking down the trail</li>
    <li><svg width="14" height="12" viewBox="0 0 14 12"><polygon points="0,0 14,6 0,12 4,6" fill="#e8141b"/></svg>Introduction to energy management &amp; flow</li>
    <li><svg width="14" height="12" viewBox="0 0 14 12"><polygon points="0,0 14,6 0,12 4,6" fill="#e8141b"/></svg>Linking trail sections for flow</li>
  </ul>
  <ul class="skills-list skills-right">
    <li><svg width="14" height="12" viewBox="0 0 14 12"><polygon points="0,0 14,6 0,12 4,6" fill="#e8141b"/></svg>Attacking flat corners</li>
    <li><svg width="14" height="12" viewBox="0 0 14 12"><polygon points="0,0 14,6 0,12 4,6" fill="#e8141b"/></svg>Flat and cambered corners</li>
    <li><svg width="14" height="12" viewBox="0 0 14 12"><polygon points="0,0 14,6 0,12 4,6" fill="#e8141b"/></svg>Bermed corners; lines and pumping</li>
    <li><svg width="14" height="12" viewBox="0 0 14 12"><polygon points="0,0 14,6 0,12 4,6" fill="#e8141b"/></svg>Switchbacks</li>
    <li><svg width="14" height="12" viewBox="0 0 14 12"><polygon points="0,0 14,6 0,12 4,6" fill="#e8141b"/></svg>Maximizing grip and traction with pumping</li>
    <li><svg width="14" height="12" viewBox="0 0 14 12"><polygon points="0,0 14,6 0,12 4,6" fill="#e8141b"/></svg>Learning to pump for speed &amp; air</li>
  </ul>

  <div class="host">
    <span class="host-label">EVENT HOSTED BY:</span>
    <span class="host-logo"><span class="dot"></span>HARLOWE CYCLE DEPOT</span>
  </div>

  <div class="footer-rule"></div>
  <footer class="footer">For more informaiton on our website:<strong>WWW.PEDALWITHPOISE.COM</strong></footer>
</main>
</body>
</html>
```